Product label

Create a hip label for a small line of products to be sold at a barbershop.
Updates

Reason: I'm extending the dead line to have improvements made....also since you guys all over the world, I want to accomadet for the day and time differences. Thank you for understanding

Target Market(s)

Men with facial hair....

Industry/Entity Type

Product

Colors

Requirements
Nice to have
• Nostalgic look, current vibe, easy to read . will need room for ingredients list on the label along with business details...website, no animal testing, made in the USA and shop logo..I'm not apposed to having the logo as a secondary feature on the label as well. Please as creative as you want to be....

```html
<!DOCTYPE html>
<html lang="en">
<head>
<meta charset="utf-8">
<title>The Corner Blade – Product Labels</title>
<link rel="stylesheet" href="https://fonts.googleapis.com/css2?family=Sorts+Mill+Goudy&display=swap">
<style>
  :root{
    --bottle:#f39120;
    --label:#f9c88e;
    --ink:#ffffff;
    --brand:#2b1a12;
    --line:#2a2017;
    --paper:#ffffff;
  }
  html,body{margin:0;padding:0;width:1200px;height:1000px;overflow:hidden;background:var(--paper);}
  .sheet{display:block;width:1200px;height:1000px;}
  .sheet text{font-family:"Sorts Mill Goudy",serif;fill:var(--ink);}
  .label-band{fill:var(--label);stroke:var(--line);stroke-width:1;}
  .bottle{fill:var(--bottle);stroke:var(--line);stroke-width:1;}
  .sheet .brand-name{fill:var(--brand);text-anchor:middle;}
  .product-name,.center{text-anchor:middle;}
  .address{text-anchor:end;}
  .rabbit-icon{fill:none;stroke:var(--ink);stroke-width:2;}
</style>
</head>
<body>
<svg class="sheet" viewBox="0 0 1200 1000" xmlns="http://www.w3.org/2000/svg">
  <defs>
    <symbol id="bottle-shape" viewBox="0 0 100 250" preserveAspectRatio="none">
      <path d="M28 0 H72 V12 H74 V28 H70 V40 C70 60 100 70 100 100 V240 Q100 250 90 250 H10 Q0 250 0 240 V100 C0 70 30 60 30 40 V28 H26 V12 H28 Z" vector-effect="non-scaling-stroke"/>
    </symbol>
    <symbol id="wave-band" viewBox="0 0 340 110" preserveAspectRatio="none" overflow="visible">
      <path d="M0 15 Q170 -5 340 15 L334 35 Q344 57 334 80 L340 100 Q170 118 0 100 L6 80 Q-4 57 6 35 Z" vector-effect="non-scaling-stroke"/>
    </symbol>
  </defs>

  <!-- Beard oil, wave label -->
  <g class="product beard-oil-wave">
    <use href="#wave-band" class="label-band" x="14" y="240" width="334" height="115"/>
    <use href="#bottle-shape" class="bottle" x="122" y="127" width="114" height="283"/>
    <text class="brand-name" x="179" y="254" font-size="12">The Corner Blade</text>
    <g class="address" font-size="9">
      <text x="118" y="268">The Corner Blade</text>
      <text x="118" y="280">1280 Elm Avenue,</text>
      <text x="118" y="292">Port Avalon CA</text>
      <text x="118" y="304">92000</text>
      <text x="118" y="316">ph: 555 014-2290</text>
      <text x="118" y="328" font-size="8.5">www.thecornerblade.com</text>
    </g>
    <text class="product-name" x="165" y="326" font-size="17">Beard Oil</text>
    <text x="212" y="330" font-size="9">2 Oz</text>
    <g class="ingredients" font-size="6">
      <text x="238" y="270">Ingredients: Lorem ipsum dolor</text>
      <text x="238" y="278">sit amet, consectetur adipiscing</text>
      <text x="238" y="286">elit, sed do eiusmod tempor</text>
      <text x="238" y="294">ut labore et dolore aliqua.</text>
    </g>
    <text x="238" y="306" font-size="9.5">Made</text>
    <text x="238" y="317" font-size="9.5">in U.S.A.</text>
    <rect class="rabbit-icon" x="288" y="302" width="26" height="20" rx="10" role="img" aria-label="Cruelty-free rabbit icon"/>
    <text x="290" y="331" font-size="7.5">Not tested</text>
    <text x="290" y="340" font-size="7.5">on animals</text>
  </g>

  <!-- Pomade, wave label -->
  <g class="product pomade-wave">
    <use href="#wave-band" class="label-band" x="258" y="400" width="400" height="148"/>
    <use href="#bottle-shape" class="bottle" x="393" y="270" width="108" height="323"/>
    <text class="brand-name" x="447" y="422" font-size="12">The Corner Blade</text>
    <g class="address" font-size="11">
      <text x="390" y="440">The Corner Blade</text>
      <text x="390" y="453">1280 Elm Avenue,</text>
      <text x="390" y="466">Port Avalon CA</text>
      <text x="390" y="479">92000</text>
      <text x="390" y="492">ph: 555 014-2290</text>
      <text x="390" y="505">www.thecornerblade.com</text>
    </g>
    <text class="product-name" x="445" y="511" font-size="22">Pomade</text>
    <text x="508" y="517" font-size="10">4 Oz</text>
    <g class="ingredients" font-size="7">
      <text x="537" y="443">Ingredients: Lorem ipsum dolor sit</text>
      <text x="537" y="454">amet, consectetur adipiscing elit,</text>
      <text x="537" y="465">sed do eiusmod tempor incididunt</text>
      <text x="537" y="476">ut labore et dolore magna aliqua.</text>
    </g>
    <text x="537" y="499" font-size="12">Made</text>
    <text x="537" y="514" font-size="12">in U.S.A.</text>
    <rect class="rabbit-icon" x="598" y="474" width="32" height="26" rx="13" role="img" aria-label="Cruelty-free rabbit icon"/>
    <text x="603" y="520" font-size="8.5">Not tested</text>
    <text x="603" y="531" font-size="8.5">on animals</text>
  </g>

  <!-- Shampoo, wave label -->
  <g class="product shampoo-wave">
    <use href="#wave-band" class="label-band" x="668" y="190" width="522" height="168"/>
    <use href="#bottle-shape" class="bottle" x="838" y="20" width="168" height="393"/>
    <text class="brand-name" x="922" y="203" font-size="19">The Corner Blade</text>
    <g class="address" font-size="14">
      <text x="832" y="226">The Corner Blade</text>
      <text x="832" y="245">1280 Elm Avenue,</text>
      <text x="832" y="264">Port Avalon CA</text>
      <text x="832" y="283">92000</text>
      <text x="832" y="302">ph: 555 014-2290</text>
      <text x="832" y="319" font-size="12">www.thecornerblade.com</text>
    </g>
    <text class="product-name" x="902" y="314" font-size="28">Shampoo</text>
    <text x="975" y="323" font-size="13">8 Oz</text>
    <g class="ingredients" font-size="9">
      <text x="1016" y="229">Ingredients: Lorem ipsum dolor sit</text>
      <text x="1016" y="243">amet, consectetur adipiscing elit,</text>
      <text x="1016" y="257">sed do eiusmod tempor incididunt</text>
      <text x="1016" y="271">ut labore et dolore magna aliqua.</text>
    </g>
    <text x="1016" y="300" font-size="15">Made</text>
    <text x="1016" y="321" font-size="15">in U.S.A.</text>
    <rect class="rabbit-icon" x="1092" y="276" width="40" height="32" rx="16" role="img" aria-label="Cruelty-free rabbit icon"/>
    <text x="1098" y="326" font-size="11">Not tested</text>
    <text x="1098" y="340" font-size="11">on animals</text>
  </g>

  <!-- Beard oil, rectangular label -->
  <g class="product beard-oil-rect">
    <rect class="label-band" x="5" y="618" width="333" height="123"/>
    <use href="#bottle-shape" class="bottle" x="117" y="522" width="108" height="283"/>
    <text class="brand-name" x="171" y="642" font-size="12">The Corner Blade</text>
    <g class="contact" font-size="9">
      <text x="9" y="641">The Corner Blade</text>
      <text x="9" y="653">1280 Elm Avenue,</text>
      <text x="9" y="665">Port Avalon CA</text>
      <text x="9" y="677">92000</text>
      <text x="9" y="689">ph: 555 014-2290</text>
      <text x="9" y="701" font-size="8.5">www.thecornerblade.com</text>
    </g>
    <text class="product-name" x="171" y="679" font-size="18">Beard Oil</text>
    <text x="205" y="738" font-size="9">2 Oz</text>
    <g class="ingredients" font-size="6">
      <text x="236" y="630">Ingredients: Lorem ipsum dolor</text>
      <text x="236" y="638">sit amet, consectetur adipiscing</text>
      <text x="236" y="646">elit, sed do eiusmod tempor</text>
      <text x="236" y="654">ut labore et dolore aliqua.</text>
    </g>
    <text x="236" y="667" font-size="10">Made in U.S.A.</text>
    <rect class="rabbit-icon" x="281" y="686" width="26" height="20" rx="10" role="img" aria-label="Cruelty-free rabbit icon"/>
    <text x="278" y="724" font-size="8">Not tested</text>
    <text x="278" y="734" font-size="8">on animals</text>
  </g>

  <!-- Pomade, rectangular label -->
  <g class="product pomade-rect">
    <rect class="label-band" x="239" y="773" width="422" height="175"/>
    <use href="#bottle-shape" class="bottle" x="380" y="676" width="140" height="322"/>
    <text class="brand-name" x="450" y="804" font-size="15">The Corner Blade</text>
    <g class="contact" font-size="12">
      <text x="244" y="808">The Corner Blade</text>
      <text x="244" y="825">1280 Elm Avenue,</text>
      <text x="244" y="842">Port Avalon CA</text>
      <text x="244" y="859">92000</text>
      <text x="244" y="876">ph: 555 014-2290</text>
      <text x="244" y="893">www.thecornerblade.com</text>
    </g>
    <text class="product-name" x="450" y="862" font-size="24">Pomade</text>
    <text x="494" y="943" font-size="11">4 Oz</text>
    <g class="ingredients" font-size="7.5">
      <text x="531" y="793">Ingredients: Lorem ipsum dolor sit</text>
      <text x="531" y="805">amet, consectetur adipiscing elit,</text>
      <text x="531" y="817">sed do eiusmod tempor incididunt</text>
      <text x="531" y="829">ut labore et dolore magna aliqua.</text>
    </g>
    <text x="531" y="846" font-size="13">Made in U.S.A.</text>
    <rect class="rabbit-icon" x="586" y="877" width="32" height="26" rx="13" role="img" aria-label="Cruelty-free rabbit icon"/>
    <text x="586" y="925" font-size="9">Not tested</text>
    <text x="586" y="938" font-size="9">on animals</text>
  </g>

  <!-- Shampoo, rectangular label -->
  <g class="product shampoo-rect">
    <rect class="label-band" x="671" y="578" width="518" height="207"/>
    <use href="#bottle-shape" class="bottle" x="847" y="438" width="168" height="393"/>
    <text class="brand-name" x="931" y="614" font-size="19">The Corner Blade</text>
    <g class="contact" font-size="15">
      <text x="677" y="620">The Corner Blade</text>
      <text x="677" y="641">1280 Elm Avenue,</text>
      <text x="677" y="661">Port Avalon CA</text>
      <text x="677" y="681">92000</text>
      <text x="677" y="701">ph: 555 014-2290</text>
      <text x="677" y="721">www.thecornerblade.com</text>
    </g>
    <text class="product-name" x="931" y="684" font-size="28">Shampoo</text>
    <text x="1012" y="776" font-size="13">8 Oz</text>
    <g class="ingredients" font-size="9">
      <text x="1032" y="601">Ingredients: Lorem ipsum dolor sit</text>
      <text x="1032" y="613">amet, consectetur adipiscing elit,</text>
      <text x="1032" y="625">sed do eiusmod tempor incididunt</text>
      <text x="1032" y="637">ut labore et dolore magna aliqua.</text>
    </g>
    <text x="1032" y="663" font-size="16">Made in U.S.A.</text>
    <rect class="rabbit-icon" x="1100" y="697" width="40" height="32" rx="16" role="img" aria-label="Cruelty-free rabbit icon"/>
    <text x="1096" y="760" font-size="11">Not tested</text>
    <text x="1096" y="776" font-size="11">on animals</text>
  </g>
</svg>
</body>
</html>
```